Web Design Project for hueframe

We are looking for a sleek and sophisticated website design for our already developed web-based gallery management software application. Here is a link to our web-app: http://www.hue-frame.co

You will login on the main page and then we would like to include all of the information on the PDF that I am providing below (it outlines what?, where?, why? who? and how much?). Basically, we need a home page, about page, and a pricing page, as well as a sign up page that should be navigable from the upper right hand corner of the site where the sign in/sign up would be located. Also, our 3 tenets are that the software program is "attractive, accessible, and affordable", which might need to be somehow incorporated. There are a few websites that we would like for you to take inspiration from listed below:

https://mybrolvex.com (for homepage)
https://pillowmantic.com (for homepage/pricing page/etc)
https://mybrolvex.com/tour (for a tour of how the product works)

We are currently having a logo designed and will share that as soon as it is available! Also, let us know if you need photos/screen shots, as we can provide them.

Thanks!

Target Market(s)

art galleries, artists, art collectors, art consultants, museums

Industry/Entity Type

Software

Requirements
Must have
• Home page
About page (or tour through the app)
Pricing page
Sign up page (the more click-throughs to signing up the better)

```html
<!DOCTYPE html>
<html lang="en">
<head>
<meta charset="utf-8">
<title>hueframe – manage your art data on the cloud</title>
<link rel="stylesheet" href="https://fonts.googleapis.com/css2?family=Arimo:ital,wght@0,400;0,700;1,400&family=Lobster&display=swap">
<style>
  :root {
    --sky: #43c0e7;
    --sky-light: #8fd6f2;
    --teal: #216f85;
    --teal-deep: #1d6579;
    --teal-soft: #3d8699;
    --orange: #f07a32;
    --orange-dark: #d8621f;
    --paper: #f3f4f5;
    --ink: #444444;
    --muted: #8a8f93;
    --white: #ffffff;
    --line: #dcdfe2;
  }
  * { box-sizing: border-box; margin: 0; padding: 0; }
  html, body { width: 1020px; height: 1200px; overflow: hidden; }
  body {
    position: relative;
    font-family: "Arimo", Arial, sans-serif;
    background: var(--paper);
    color: var(--ink);
  }
  .abs { position: absolute; }

  /* header */
  .site-header {
    position: absolute; left: 0; top: 0; width: 1020px; height: 73px;
    background: var(--sky); border-bottom: 3px solid var(--white);
  }
  .brand { position: absolute; left: 52px; top: 17px; display: flex; align-items: center; gap: 14px; }
  .brand-dot { width: 40px; height: 40px; border-radius: 50%; border: 3px solid var(--white); }
  .brand-name { color: var(--white); font-size: 26px; letter-spacing: 0.5px; }
  .main-nav { position: absolute; left: 339px; top: 0; display: flex; height: 70px; }
  .main-nav a {
    color: var(--white); text-decoration: none; font-size: 17px;
    line-height: 70px; padding: 0 15px 0 0;
  }
  .main-nav a.is-active { background: var(--teal); padding: 0 21px 0 22px; margin-right: 15px; }
  .login { position: absolute; left: 727px; top: 25px; display: flex; gap: 8px; align-items: center; }
  .login span.field {
    width: 103px; height: 21px; background: var(--white); border-radius: 2px;
    font-size: 12px; color: #777; padding: 3px 6px;
  }
  .login .go { color: var(--white); font-size: 15px; margin-left: 0; }

  /* hero */
  .hero-photo {
    position: absolute; left: 0; top: 73px; width: 1020px; height: 367px;
    background: linear-gradient(180deg, #151515 0%, #3c3c3c 35%, #9a9a9a 70%, #cfcfcf 100%);
  }
  .hero-title {
    position: absolute; left: 273px; top: 103px; font-size: 50px; letter-spacing: -2px;
    color: var(--white); text-shadow: 2px 2px 4px rgba(0,0,0,.6); white-space: nowrap;
  }
  .hero-title .accent { color: var(--sky-light); }
  .hero-rule { position: absolute; left: 277px; top: 156px; width: 468px; height: 2px; background: #777; }
  .hero-lead {
    position: absolute; left: 278px; top: 178px; font-size: 32px; line-height: 29px;
    color: var(--white); letter-spacing: -1px; text-shadow: 2px 2px 4px rgba(0,0,0,.6);
  }
  .cta {
    position: absolute; left: 398px; top: 248px; width: 209px; height: 45px;
    background: var(--sky); color: var(--white); font-size: 20px; text-align: center;
    line-height: 45px; border-radius: 2px;
  }

  /* features */
  .feature {
    position: absolute; top: 328px; width: 214px; height: 214px; border-radius: 50%;
    background: var(--white); box-shadow: 0 2px 6px rgba(0,0,0,.15);
  }
  .feature-inner {
    position: absolute; left: 14px; top: 14px; width: 186px; height: 186px; border-radius: 50%;
    background: var(--teal);
  }
  .feature svg { position: absolute; left: 0; top: 0; }
  .feature-label {
    position: absolute; left: 0; width: 186px; top: 153px; text-align: center;
    color: var(--white); font-size: 16px;
  }

  /* how it works */
  .ribbon { position: absolute; left: 288px; top: 611px; }
  .ribbon-text {
    position: absolute; left: 326px; top: 612px; width: 368px; height: 43px;
    line-height: 43px; text-align: center; color: var(--white); font-size: 16px;
  }
  .how-title {
    position: absolute; left: 0; width: 1040px; top: 678px; text-align: center;
    font-family: "Lobster", cursive; font-size: 21px; color: var(--ink);
  }
  .wave { position: absolute; left: 0; top: 0; }
  .step {
    position: absolute; top: 726px; width: 157px; height: 106px; background: var(--white);
    border: 1px solid var(--line); border-radius: 4px; padding: 17px 0 0 20px;
  }
  .step h3 {
    font-weight: 400; font-style: italic; font-size: 20px; color: var(--teal);
    text-align: center; margin-left: -20px; margin-bottom: 4px;
  }
  .step p { font-size: 13px; line-height: 16px; color: var(--muted); letter-spacing: -0.3px; }
  .step-arrow {
    position: absolute; top: 760px; width: 37px; height: 37px; border-radius: 50%;
    background: var(--white); border: 2px solid var(--line);
  }

  /* video */
  .video { position: absolute; left: 264px; top: 860px; width: 483px; height: 249px;
    box-shadow: 0 2px 6px rgba(0,0,0,.35); }
  .video-still { position: absolute; inset: 0; background: linear-gradient(180deg, #f2f3f5, #e3e6ea); }
  .video svg { position: absolute; left: 0; top: 0; }
  .video-time { position: absolute; left: 111px; top: 213px; font-size: 11px; color: var(--white); }

  /* footer */
  .site-footer { position: absolute; left: 0; top: 1170px; width: 1020px; color: var(--white); font-size: 14px; letter-spacing: -0.4px; }
  .footer-nav { position: absolute; left: 25px; top: 0; white-space: nowrap; }
  .footer-nav .sep { margin: 0 12px; }
  .copyright { position: absolute; left: 395px; top: 0; white-space: nowrap; }
  .follow { position: absolute; left: 861px; top: 0; display: flex; align-items: center; gap: 4px; }
  .follow .social { width: 17px; height: 17px; background: #7fc4e6; border-radius: 2px; }
  .follow .social.second { background: #4d6fa8; margin-left: -2px; }
  .follow span.label { margin-right: 8px; }
</style>
</head>
<body>

<header class="site-header">
  <div class="brand"><span class="brand-dot"></span><span class="brand-name">hueframe</span></div>
  <nav class="main-nav">
    <a class="is-active" href="#">Home</a>
    <a href="#">About</a>
    <a href="#">Pricing</a>
    <a href="#">Sign up</a>
  </nav>
  <div class="login">
    <span class="field">username</span>
    <span class="field">password</span>
    <span class="go">Go</span>
  </div>
</header>

<div class="hero-photo" role="img" aria-label="Black and white photograph of an art gallery interior with framed portraits on the walls"></div>
<h1 class="hero-title">Welcome to <span class="accent">hueFRAME</span></h1>
<div class="hero-rule"></div>
<p class="hero-lead">the easiest way to manage your<br>art data on the cloud.</p>
<a class="cta">LEARN MORE</a>

<svg class="wave" width="1020" height="1200" aria-hidden="true">
  <defs>
    <linearGradient id="teal-fade" x1="0" y1="0" x2="0" y2="1">
      <stop offset="0" stop-color="#1f687c"/>
      <stop offset="1" stop-color="#3e8698"/>
    </linearGradient>
  </defs>
  <path d="M0 836 Q510 728 1020 836 L1020 1200 L0 1200 Z" fill="url(#teal-fade)"/>
</svg>

<div class="feature" style="left:158px">
  <div class="feature-inner">
    <svg width="186" height="186" aria-hidden="true">
      <g transform="rotate(25 58 78)">
        <rect x="36" y="50" width="42" height="66" rx="7" fill="#eef1f3"/>
        <rect x="42" y="58" width="30" height="46" fill="#000"/>
        <circle cx="57" cy="110" r="3" fill="#43c0e7"/>
      </g>
      <rect x="98" y="44" width="46" height="82" rx="5" fill="#000"/>
      <rect x="102" y="52" width="38" height="62" fill="#fff"/>
      <circle cx="121" cy="120" r="3" fill="#43c0e7"/>
    </svg>
    <div class="feature-label">PORTABLE</div>
  </div>
</div>

<div class="feature" style="left:403px">
  <div class="feature-inner">
    <svg width="186" height="186" aria-hidden="true">
      <rect x="41" y="47" width="104" height="80" rx="6" fill="#f2f2f2"/>
      <rect x="50" y="53" width="86" height="66" fill="#000"/>
      <circle cx="45" cy="87" r="2.5" fill="#43c0e7"/>
    </svg>
    <div class="feature-label">COMFORTABLE</div>
  </div>
</div>

<div class="feature" style="left:647px">
  <div class="feature-inner">
    <svg width="186" height="186" aria-hidden="true">
      <rect x="38" y="32" width="110" height="86" rx="4" fill="#eceeef"/>
      <rect x="45" y="39" width="96" height="66" fill="#000"/>
      <path d="M84 118 L102 118 L106 134 L80 134 Z" fill="#cfd3d6"/>
      <rect x="74" y="133" width="38" height="4" rx="2" fill="#e6e8ea"/>
    </svg>
    <div class="feature-label">SATISFACTION</div>
  </div>
</div>

<svg class="ribbon" width="442" height="56" aria-hidden="true">
  <path d="M2 20 L55 20 L55 54 L2 54 L20 37 Z" fill="var(--orange-dark)"/>
  <path d="M440 20 L387 20 L387 54 L440 54 L422 37 Z" fill="var(--orange-dark)"/>
  <rect x="38" y="1" width="368" height="43" fill="var(--orange)"/>
</svg>
<div class="ribbon-text">CONNECT ANYTIME, ANYWHERE</div>

<h2 class="how-title">How does it work?</h2>

<div class="step" style="left:257px">
  <h3>UPLOAD</h3>
  <p>Lorem ipsum dolor sit amet, consectetur tatbu eksalu adipiscing elit.</p>
</div>
<div class="step" style="left:429px">
  <h3>STORAGE</h3>
  <p>Lorem ipsum dolor sit sectetur tatbu ekusora adipiscing elit.</p>
</div>
<div class="step" style="left:601px">
  <h3>DELIVERY</h3>
  <p>Lorem ipsum dolor sit amet, consectetur</p>
</div>

<svg class="step-arrow" style="left:401px" viewBox="0 0 37 37" aria-hidden="true">
  <path d="M14 10 L23 18.5 L14 27" fill="none" stroke="var(--teal)" stroke-width="4"/>
</svg>
<svg class="step-arrow" style="left:573px" viewBox="0 0 37 37" aria-hidden="true">
  <path d="M14 10 L23 18.5 L14 27" fill="none" stroke="var(--teal)" stroke-width="4"/>
</svg>

<div class="video">
  <div class="video-still" role="img" aria-label="Video still of the hueframe web app showing an artwork list table in a browser window"></div>
  <svg width="483" height="249" aria-hidden="true">
    <rect x="228" y="104" width="39" height="38" rx="3" fill="#222"/>
    <path d="M241 114 L256 123 L241 132 Z" fill="#fff"/>
    <rect x="33" y="196" width="58" height="38" rx="3" fill="#222"/>
    <path d="M55 206 L72 215 L55 224 Z" fill="#fff"/>
    <rect x="103" y="206" width="358" height="28" rx="3" fill="#222" opacity=".92"/>
    <rect x="147" y="215" width="229" height="9" fill="none" stroke="#fff" stroke-width="1.5"/>
    <g fill="#fff">
      <rect x="384" y="214" width="3" height="11"/><rect x="389" y="214" width="3" height="11"/>
      <rect x="394" y="214" width="3" height="11"/><rect x="399" y="214" width="3" height="11"/>
      <rect x="404" y="214" width="3" height="11"/><rect x="409" y="214" width="3" height="11"/>
      <rect x="414" y="214" width="3" height="11"/>
    </g>
    <rect x="420" y="214" width="9" height="11" fill="#777"/>
    <g fill="none" stroke="#fff" stroke-width="1.6">
      <path d="M440 214 h4 M440 214 v4 M452 214 h-4 M452 214 v4 M440 226 h4 M440 226 v-4 M452 226 h-4 M452 226 v-4 M441 215 l10 10 M451 215 l-10 10"/>
    </g>
  </svg>
  <span class="video-time">00:00</span>
</div>

<footer class="site-footer">
  <nav class="footer-nav">Home<span class="sep">|</span>About<span class="sep">|</span>Pricing<span class="sep">|</span>Sitemap</nav>
  <p class="copyright">Copyright hueframe 20013 All rights reserved</p>
  <div class="follow"><span class="label">Follow us</span><span class="social"></span><span class="social second"></span></div>
</footer>

</body>
</html>
```